Concrete Finishing business needs new business card and a logo design

We are a family owned and operated, concrete finishing business. 2020 marks our 33 rd year in business. We operate under Harold M. Ferrick and Sons Concrete Contractors Ltd. Harold M was my father and founder of the company. We usually shorten the name and use H M Ferrick & Sons Ltd. Most people in the Concrete Finishing industry tend to know us by our last name 'Ferrick' . in honour of our father, we would still like to have his name on the cards and logo but are open to shortening it to H.M (maybe in a small font with the W on top of the J ) and focusing more on the "Ferrick & Sons."....Or maybe something with just the initials HMF...or if you could use the "J" and somehow incorporate an artistic drawing/shape of a 'power trowel' (what we use apply a smooth finish to the concrete with) but still visually see that its a J, would be cool. Would like to see designs using Black with silver or grey lettering but are open to other ideas. Seen a business card online with the front of the business card looking like concrete and with just the word CONCRETE on it... On the back was the company name , address and contact info of the company....looked really good! i clicked doubled sided in case of something like that but we are open to just single sided as well. After viewing some of the designs, maybe a pop of colour would be nice ... open to any ideas and colours.😊

Target Market(s)

Construction

```html
<!DOCTYPE html>
<html lang="en">
<head>
<meta charset="utf-8">
<title>Business Card – Concrete Floor Finishing</title>
<link href="https://fonts.googleapis.com/css2?family=Oswald:wght@600&family=Arimo:wght@400&display=swap" rel="stylesheet">
<style>
  :root {
    --backdrop: #2a2a2a;
    --card-black: #1b1b1b;
    --card-white: #ffffff;
    --ink: #111111;
    --paper: #ffffff;
    --rule: #d6d6d6;
  }
  * { box-sizing: border-box; margin: 0; padding: 0; }
  html, body {
    width: 1200px; height: 1015px; overflow: hidden;
    background: var(--backdrop);
  }
  .stage { position: relative; width: 1200px; height: 1015px; }
  .card {
    position: absolute; left: 280px; width: 640px; height: 366px;
    box-shadow: 0 10px 30px rgba(0,0,0,.5);
  }
  .card--front { top: 120px; background: var(--card-black); color: var(--paper); }
  .card--back  { top: 530px; background: var(--card-white); color: var(--ink); }

  .brand {
    display: flex; align-items: center; gap: 14px;
    font-family: "Arimo", sans-serif; font-weight: 400;
    line-height: 1; white-space: nowrap;
  }
  .brand__square { width: 20px; height: 20px; background: currentColor; flex: none; }

  .card--front .brand { position: absolute; left: 132px; top: 140px; font-size: 38px; }
  .tagline {
    position: absolute; left: 132px; top: 214px;
    font-family: "Arimo", sans-serif; font-size: 15px; letter-spacing: 2.2px;
    text-transform: uppercase;
  }

  .card--back .brand { position: absolute; left: 46px; top: 168px; font-size: 26px; gap: 10px; }
  .card--back .brand__square { width: 15px; height: 15px; }
  .divider {
    position: absolute; left: 366px; top: 58px; width: 1px; height: 250px;
    background: var(--rule);
  }
  .contact {
    position: absolute; left: 392px; top: 62px;
    font-family: "Arimo", sans-serif; font-size: 16px; line-height: 1.25;
  }
  .contact__name {
    font-family: "Oswald", sans-serif; font-weight: 600; font-size: 26px;
    text-transform: uppercase; line-height: 1.05;
  }
  .contact__title { margin-bottom: 14px; }
  .contact__list { list-style: none; margin-bottom: 18px; }
  .contact__list li { display: flex; align-items: center; gap: 8px; }
  .contact__list svg { width: 14px; height: 14px; flex: none; fill: var(--ink); }
</style>
</head>
<body>
<main class="stage">
  <section class="card card--front">
    <div class="brand"><span class="brand__square"></span>Ferrick &amp; Sons</div>
    <p class="tagline">Specializing in concrete floor finishing</p>
  </section>

  <section class="card card--back">
    <div class="brand"><span class="brand__square"></span>Ferrick &amp; Sons</div>
    <div class="divider"></div>
    <div class="contact">
      <p class="contact__name">Martin Kealey</p>
      <p class="contact__title">Managing Director</p>
      <ul class="contact__list">
        <li><svg viewBox="0 0 14 14" aria-hidden="true"><path d="M3 0h8a1 1 0 0 1 1 1v12a1 1 0 0 1-1 1H3a1 1 0 0 1-1-1V1a1 1 0 0 1 1-1zm0 2v9h8V2z"/></svg>(709)555-0142</li>
        <li><svg viewBox="0 0 14 14" aria-hidden="true"><path d="M3 1l2 3-1.3 1.3a8 8 0 0 0 5 5L10 9l3 2-1 2.5C6 13.5.5 8 .5 2z"/></svg>(709)555-0178</li>
        <li><svg viewBox="0 0 14 14" aria-hidden="true"><path d="M3 0h6v4H3zM1 5h12v6h-2v3H3v-3H1zm3 4v3h6V9z"/></svg>(709)555-0193</li>
        <li><svg viewBox="0 0 14 14" aria-hidden="true"><path d="M0 3h14v9H0zm1 1v.5l6 4 6-4V4z"/></svg>office@kealeyfloors.ca</li>
      </ul>
      <p>P.O.Box 41, Site 9, RR#2</p>
      <p>Pine Harbour, NL</p>
      <p>A0K 2B0</p>
    </div>
  </section>
</main>
</body>
</html>
```